Wine label Design

We are looking to develop an elegant contemporary Chilean design; for a new Wine Brand ZORIVEN to be sold in Chinese Market.
We would like to see designs that are a fine balance between having a traditional design that can offer quality reassurance and being distinctive enough to stand out on crowded shelves. The final design should be easy-to-remember and communicate Quality, Tradition and have a conection with Chile.

Target Market(s)

Urban Chinese between 25 to 40 yo

Requirements
Must have
• Paper label
Information on Front label : Grape (example Cabernet sauvignon) / Vintage (ex 2010) / Wine of Chile
Bottle shape is given (see attached)
Nice to have
• An element of uniqueness, easy to recall the brand
Red and Gold Color are appreciated by the Target
Should not have
• White background
Number 4 is considered death, should not be included on the design

```html
<!DOCTYPE html>
<html lang="en">
<head>
<meta charset="utf-8">
<title>ZORIVEN Cabernet Sauvignon Label</title>
<link rel="stylesheet" href="https://fonts.googleapis.com/css2?family=Cinzel:wght@400;500&display=swap">
<style>
  :root {
    --backdrop: #e9e4dc;
    --paper-light: #f7f0dc;
    --paper-mid: #eee2c3;
    --paper-edge: #d2bf97;
    --ink-gold: #8c6b3c;
    --ink-soft: #a88a5c;
    --scene-light: #e6dcc4;
    --scene-mid: #b9ae98;
    --scene-dark: #8e8576;
  }
  html, body {
    margin: 0;
    padding: 0;
    width: 789px;
    height: 1200px;
    overflow: hidden;
    background: var(--backdrop);
  }
  .canvas {
    position: relative;
    width: 789px;
    height: 1200px;
  }
  .wine-label {
    position: absolute;
    left: 120px;
    top: 230px;
    width: 550px;
    height: 740px;
    border-radius: 22px;
    background: radial-gradient(ellipse at 50% 45%, var(--paper-light) 0%, var(--paper-mid) 72%, var(--paper-edge) 100%);
    box-shadow: 0 0 0 2px rgba(140,107,60,0.22) inset;
    font-family: "Cinzel", serif;
    color: var(--ink-gold);
    text-align: center;
  }
  .brand-name {
    position: absolute;
    top: 62px;
    left: 0;
    right: 0;
    margin: 0;
    font-size: 78px;
    font-weight: 400;
    letter-spacing: 5px;
    line-height: 1;
  }
  .rule {
    position: absolute;
    left: 80px;
    right: 80px;
    height: 1.5px;
    background: var(--ink-soft);
    opacity: 0.65;
  }
  .rule-top { top: 170px; }
  .rule-bottom { top: 430px; }
  .vineyard-scene {
    position: absolute;
    top: 186px;
    left: 80px;
    right: 80px;
    height: 228px;
    border-radius: 6px;
    background:
      linear-gradient(180deg, var(--scene-light) 0%, var(--scene-mid) 45%, var(--scene-dark) 70%, var(--scene-mid) 88%, var(--scene-light) 100%);
    opacity: 0.75;
  }
  .varietal {
    position: absolute;
    top: 500px;
    left: 0;
    right: 0;
    margin: 0;
    font-size: 28px;
    font-weight: 400;
    letter-spacing: 2px;
  }
  .vintage {
    position: absolute;
    top: 544px;
    left: 0;
    right: 0;
    margin: 0;
    font-size: 22px;
    letter-spacing: 3px;
  }
  .origin {
    position: absolute;
    top: 610px;
    left: 0;
    right: 0;
    margin: 0;
    font-size: 15px;
    letter-spacing: 5px;
    color: var(--ink-soft);
  }
</style>
</head>
<body>
<main class="canvas">
  <section class="wine-label">
    <h1 class="brand-name">ZORIVEN</h1>
    <div class="rule rule-top"></div>
    <div class="vineyard-scene" role="img" aria-label="Sepia sketch of vineyard rows stretching toward the horizon"></div>
    <div class="rule rule-bottom"></div>
    <p class="varietal">Cabernet Sauvignon</p>
    <p class="vintage">2010</p>
    <p class="origin">WINE OF CHILE</p>
  </section>
</main>
</body>
</html>
```